Dovenmarch Luxury Landscapes

A landscape business card.

Target Market(s)

Middle aged and up. Professionals.

Industry/Entity Type

Landscape

Contact Information for Business Card

Thornbeck

Colors
0054AA
0677BA
7BADD7
CADEEF
E8F1F8
0094D4
00A9DD
6FCCEA
C7EBF8
E9F6FB

Requirements
Must have
• The color blue and silver be very attractive
Nice to have
• An embossed logo. A watermark of a plant or something that indicates that we are a landscape company in the background of the backside where list of services are offered. . List of services on the back.
Should not have
• Red, yellow, orange.

```html
<!DOCTYPE html>
<html lang="en">
<head>
<meta charset="utf-8">
<title>Dovenmarch Luxury Landscapes – Business Card</title>
<link href="https://fonts.googleapis.com/css2?family=Montserrat:wght@400;500;700&family=Marcellus&display=swap" rel="stylesheet">
<style>
  :root {
    --stage: #d3d3cf;
    --paper: #eaeae6;
    --ink: #2a2a2a;
    --royal: #0316c2;
    --royal-deep: #0212a8;
    --royal-light: #1a4fe0;
    --white: #ffffff;
    --silver-light: #f4f4f2;
    --silver: #c4c4c4;
    --silver-dark: #a9a9a9;
  }
  * { margin: 0; padding: 0; box-sizing: border-box; }
  html, body { width: 1200px; height: 801px; overflow: hidden; }
  body {
    background: var(--stage);
    font-family: "Montserrat", sans-serif;
    position: relative;
  }
  .card {
    position: absolute;
    top: 258px;
    width: 500px;
    height: 286px;
    box-shadow: 0 10px 24px rgba(0,0,0,0.18);
    overflow: hidden;
  }
  .card--contact { left: 60px; background: var(--paper); }
  .card--brand {
    left: 640px;
    background: linear-gradient(135deg, var(--royal) 0%, var(--royal-deep) 100%);
  }

  .emboss-mark {
    position: absolute;
    left: 52px;
    top: 58px;
    width: 170px;
    height: 170px;
    border-radius: 50%;
    background: radial-gradient(circle at 35% 30%, var(--silver-light) 0%, var(--silver) 60%, var(--silver-dark) 100%);
    box-shadow: inset 2px 3px 6px rgba(255,255,255,0.7), inset -3px -4px 8px rgba(0,0,0,0.12);
    opacity: 0.75;
  }

  .contact {
    position: absolute;
    left: 250px;
    top: 58px;
    color: var(--ink);
    font-size: 11.5px;
    line-height: 1.45;
  }
  .contact__name {
    color: var(--royal);
    font-weight: 700;
    font-size: 17px;
    letter-spacing: 0.02em;
    margin-bottom: 8px;
  }
  .contact__row { display: flex; align-items: center; gap: 6px; }
  .contact__icon { width: 9px; height: 9px; flex: none; }
  .contact__address { margin-top: 10px; }

  .foil-mark {
    position: absolute;
    left: 262px;
    top: 22px;
    width: 150px;
    height: 150px;
    border-radius: 50%;
    background: radial-gradient(circle at 65% 30%, var(--royal-light) 0%, var(--royal) 55%, var(--royal-deep) 100%);
    box-shadow: inset 0 0 10px rgba(0,0,20,0.25);
  }

  .brand-name {
    position: absolute;
    left: 44px;
    bottom: 44px;
    color: var(--white);
    font-family: "Marcellus", serif;
    font-weight: 400;
    line-height: 1.05;
  }
  .brand-name__main { font-size: 40px; letter-spacing: 0.03em; }
  .brand-name__sub { font-size: 16px; letter-spacing: 0.14em; margin-top: 4px; }
</style>
</head>
<body>

  <section class="card card--contact">
    <div class="emboss-mark" role="img" aria-label="Embossed silver monogram mark"></div>
    <div class="contact">
      <p class="contact__name">CARLA WENDOVER</p>
      <p class="contact__row">
        <svg class="contact__icon" viewBox="0 0 10 10"><path d="M2 1 L4 1 L4.6 3 L3.4 3.8 Q4.4 5.8 6.2 6.6 L7 5.4 L9 6 L9 8 Q5 9 1.6 4.4 Q1 2.6 2 1Z" fill="var(--royal)"/></svg>
        902-555-0147
      </p>
      <p class="contact__row">
        <svg class="contact__icon" viewBox="0 0 10 10"><rect x="0.8" y="2" width="8.4" height="6" fill="none" stroke="var(--royal)" stroke-width="1.1"/><path d="M0.8 2 L5 5.4 L9.2 2" fill="none" stroke="var(--royal)" stroke-width="1.1"/></svg>
        info@dovenmarchluxury.com
      </p>
      <p class="contact__row">
        <svg class="contact__icon" viewBox="0 0 10 10"><circle cx="5" cy="5" r="4.3" fill="var(--royal)"/><path d="M0.7 5 H9.3 M5 0.7 V9.3" stroke="var(--paper)" stroke-width="0.7"/></svg>
        www.dovenmarchluxury.com
      </p>
      <p class="contact__address">18B Hollis Mill Road, Thornbeck<br>Nova Scotia, B3K 4M2</p>
    </div>
  </section>

  <section class="card card--brand">
    <div class="foil-mark" role="img" aria-label="Blue foil monogram mark"></div>
    <div class="brand-name">
      <p class="brand-name__main">DOVENMARCH</p>
      <p class="brand-name__sub">LUXURY LANDSCAPES</p>
    </div>
  </section>

</body>
</html>
```